Brochure Design Project law firm

we require a print brochure for marketing. the information is contained on our website www.brindlecourt.com.au
we need to appeal to smash repairers who do third party claims. which means, where a person has had a car accident where it is not their fault they want their car fixed by the smash repairer who agrees to do the repairs and then claims the money from the insurer directly.

we will need a logo and business cards too.

Industry/Entity Type

Law Firm

Requirements
Must have
• pictures, law firm and smash repairer related.

```html
<!DOCTYPE html>
<html lang="en">
<head>
<meta charset="utf-8">
<title>Brindle Court Lawyers – Repairer Brochure, Inside Spread</title>
<link rel="stylesheet" href="https://fonts.googleapis.com/css2?family=Open+Sans:wght@400;600;700;800&display=swap">
<style>
  :root {
    --page-bg: #eeeeee;
    --brochure-red: #c52d3a;
    --brochure-red-dark: #a92230;
    --brochure-yellow: #f3e22f;
    --text-light: #ffffff;
    --fold-shadow: rgba(0, 0, 0, 0.14);
  }
  * { box-sizing: border-box; margin: 0; padding: 0; }
  html, body {
    width: 1200px;
    height: 900px;
    overflow: hidden;
    background: var(--page-bg);
    font-family: "Open Sans", Arial, sans-serif;
  }
  .spread {
    position: absolute;
    left: 45px;
    top: 60px;
    width: 1110px;
    height: 780px;
    background: var(--brochure-yellow);
    padding: 20px;
    box-shadow: 0 10px 30px rgba(0,0,0,0.18);
  }
  .spread-inner {
    position: relative;
    width: 100%;
    height: 100%;
    background: var(--brochure-red);
    display: flex;
    overflow: hidden;
  }
  .panel {
    position: relative;
    width: 33.333%;
    height: 100%;
    color: var(--text-light);
  }
  .panel + .panel { border-left: 2px solid var(--fold-shadow); }

  .panel-heading {
    color: var(--brochure-yellow);
    font-weight: 800;
    font-size: 40px;
    letter-spacing: 1px;
    line-height: 1;
  }
  .panel-subheading {
    font-weight: 700;
    font-size: 17px;
    margin-bottom: 10px;
  }
  .copy p {
    font-size: 12.5px;
    line-height: 1.45;
    margin-bottom: 12px;
  }
  .copy .lead-in { font-weight: 600; }

  /* Services panel */
  .services-photo {
    position: absolute;
    left: 0;
    top: 0;
    width: 357px;
    height: 200px;
  }
  .services .panel-heading { position: absolute; left: 30px; top: 218px; }
  .services .copy { position: absolute; left: 30px; right: 30px; top: 272px; }
  .services .copy p { margin-bottom: 10px; }

  /* Commitment panel */
  .commitment .panel-heading { position: absolute; left: 30px; top: 38px; }
  .commitment .copy { position: absolute; left: 30px; right: 30px; top: 100px; }

  /* Experience panel */
  .experience .copy { position: absolute; left: 30px; right: 30px; top: 40px; }
  .experience .panel-subheading { color: var(--brochure-yellow); font-size: 16px; margin-bottom: 6px; }
  .experience-photo {
    position: absolute;
    left: 0;
    top: 0;
    width: 100%;
    height: 100%;
  }
  .frame-lines {
    position: absolute;
    inset: 0;
    width: 100%;
    height: 100%;
    pointer-events: none;
  }
</style>
</head>
<body>
  <main class="spread">
    <div class="spread-inner">

      <section class="panel services">
        <svg class="services-photo" viewBox="0 0 357 200" role="img" aria-label="Photo of a workshop team giving thumbs up">
          <defs>
            <linearGradient id="teamTones" x1="0" y1="0" x2="1" y2="1">
              <stop offset="0" stop-color="#2f3e55"/>
              <stop offset="0.5" stop-color="#6d7687"/>
              <stop offset="1" stop-color="#c9a48a"/>
            </linearGradient>
          </defs>
          <polygon points="0,0 357,0 357,110 290,190 0,190" fill="url(#teamTones)"/>
          <polyline points="0,196 293,196 357,118" fill="none" stroke="var(--brochure-yellow)" stroke-width="2"/>
        </svg>
        <h2 class="panel-heading">Services</h2>
        <div class="copy">
          <p>We focus on 3rd party recovery for motor vehicle property damage claims. We act fast, keep your clients informed, and ensure the repairer is paid in full. Our head office is located in Wattle Point.</p>
          <p>We know how important cash flow is to your workshop, so we chase every claim to keep your business going.</p>
          <p>We have state of the art systems and a team of dedicated professionals who will guide you every step of the way. We are small enough to ensure that you have personal service.</p>
          <p class="lead-in">Call us today to benefit from:</p>
          <p>A proven track record<br>Our commitment to delivering an outstanding service to all of our clients</p>
          <p>If you want the best, call us on 0400 555 218 for a free, no obligation meeting with one of our specialist lawyers.</p>
          <p>We take the fight to the big insurers to achieve the best results and ensure your rights are secured.</p>
        </div>
      </section>

      <section class="panel commitment">
        <h2 class="panel-heading">Commitment</h2>
        <div class="copy">
          <h3 class="panel-subheading">Our Mission Statement</h3>
          <p>We will strive to provide the best possible service to every repairer we work with. We will recover your costs quickly, clearly and fairly, and keep you informed throughout your claim.</p>
          <p>We will communicate with you every step of the way, listen to your needs and explain all of your options in plain language so you can make the right choice.</p>
          <p>If you want the best outcome for your customers, call our team today for a free consultation with one of our dedicated lawyers.</p>
        </div>
      </section>

      <section class="panel experience">
        <svg class="experience-photo" viewBox="0 0 368 740" preserveAspectRatio="none" role="img" aria-label="Photo of a car dashboard gauge and workshop tools">
          <defs>
            <linearGradient id="dashTones" x1="0" y1="0" x2="0.6" y2="1">
              <stop offset="0" stop-color="#3a3a3c"/>
              <stop offset="0.45" stop-color="#8b8884"/>
              <stop offset="1" stop-color="#cfc6ba"/>
            </linearGradient>
          </defs>
          <polygon points="60,300 368,300 368,740 0,740 0,360" fill="url(#dashTones)"/>
        </svg>
        <div class="copy">
          <h3 class="panel-subheading">Experience</h3>
          <p>Experience is the difference. We have over 20 years of handling claims for repairers and know exactly what insurers need to settle each file.</p>
          <h3 class="panel-subheading">Reputation</h3>
          <p>We are proud to have built a reputation for results with repairers across the state, and our practice continues to grow by word of mouth.</p>
        </div>
      </section>

      <svg class="frame-lines" viewBox="0 0 1070 740" preserveAspectRatio="none" aria-hidden="true">
        <polyline points="560,740 560,700 700,700 700,360 762,288 1070,288" fill="none" stroke="var(--brochure-yellow)" stroke-width="2"/>
      </svg>

    </div>
  </main>
</body>
</html>
```